Packaging design for high end, natural skin care line needed

Marisol Thackery Beauty needs a label design. It is a new skin care line I am launching.
For years my line Velvet Orchard Beauty was quite popular and featured in several magazines, but for personal reasons had to be shut down. Now I am launching a new line featuring VOB's top selling products, but focused solely on skin care more so than cosmetics. All products will still be handmade, but the line should still look professional-something worthy of a Brindle Market shelf!
I am branding it with my name, as I am often quoted in articles related to gluten in beauty products, so Marisol Thackery and beauty are key words.
The key products will be facial and body serums which are packaged in .5oz., 1oz. and larger amber glass bottles with black dropper tops, I will include pictures below. For dimensions, the labels can be any size that you think will work best, but need to at the least fit the 1oz. bottle, dimensions shown here http://www.corvelflask.example/amber-glass-tall-round-flask/p/QZ7K-93/
I loved the former VOB logo, but for Marisol Thackery Beauty I am looking for something more personal, more apothecary-like, and probably less colorful.
The line will be small, just a handful of products, but luxe, rich.
I am attaching photos of Velvet Orchard Beauty's packaging for your reference.
Thanks much!!

Hi Everyone! Thank you for your submissions! Please see the links I provided in the brief, I really am looking for something more technical looking, like an apothecary. And want black text on a white background, not a black background, and nothing flowery.
Thank you all!!
Marisol

Target Market(s)

My clients are primarily women of all ages, but with more of a skin care focus, and no longer a cosmetic one, I would also like to appeal to a male audience. My clients are health conscious, gluten-free, natural, paleo, or vegan, etc. Target age is probably 25-55. Products are a bit high end, priced $45-65.

Industry/Entity Type

Cosmetics

Requirements
Must have
• It must at least say Marisol Thackery, or can say Marisol Thackery Beauty, but "Beauty" is not necessary. And capitalization is open, try whatever you think serves the brand. Likely slogans or taglines that can be included but are not essential: Care for your skin. Love and care for your skin. Handmade with love in the USA. Handmade in the USA. Think modern day apothecary. Small batch scotch. Something fine, but custom, handmade.
Nice to have
• I like the aesthetic of Oribel Skin Care a bit http://www.oribelhollis.example.au/
And of Dorian Valtz as shown here http://www.pinboardia.example/pin/847302915563017442/
Also of something like this that is even customizable http://www.pinboardia.example/pin/58274106392285514/
Every product is handmade in small batches, with fine ingredients, a moderate price point of around $45-$65. And I will likely begin making custom orders. So there could be a space to say when it was made, or for whom. I would like to keep the colors classic though, I probably want to stay away from the bright pink on this one.
Should not have
• As I mentioned, probably want to stay away from a lot of color. I like black vs. gray for the text, as it will show up better in editorials. I must look good, but also photograph well. Thanks!

```html
<!DOCTYPE html>
<html lang="en">
<head>
<meta charset="utf-8">
<title>Marisol Thackery Beauty — Balancing Facial Serum Label</title>
<link href="https://fonts.googleapis.com/css2?family=Oswald:wght@400;500;600&family=Courier+Prime:wght@400;700&display=swap" rel="stylesheet">
<style>
  :root {
    --canvas-bg: #f1f0ee;
    --label-bg: #ffffff;
    --label-edge: #e0dfdc;
    --ink: #111111;
    --ink-soft: #9a9a9a;
    --rule: #6d6d6d;
  }
  html, body {
    margin: 0;
    padding: 0;
    width: 861px;
    height: 1200px;
    overflow: hidden;
    background: var(--canvas-bg);
  }
  .canvas {
    position: relative;
    width: 861px;
    height: 1200px;
  }
  .label {
    position: absolute;
    left: 190px;
    top: 179px;
    width: 480px;
    height: 842px;
    background: var(--label-bg);
    border: 1px solid var(--label-edge);
    box-sizing: border-box;
  }
  .label__url {
    position: absolute;
    left: 22px;
    bottom: 70px;
    transform-origin: left bottom;
    transform: rotate(-90deg) translateY(100%);
    font-family: 'Courier Prime', monospace;
    font-size: 17px;
    letter-spacing: 1px;
    color: var(--ink-soft);
    white-space: nowrap;
  }
  .label__url b { color: var(--ink); font-weight: 700; }
  .brand {
    position: absolute;
    left: 98px;
    top: 92px;
    display: flex;
    align-items: flex-start;
    gap: 18px;
  }
  .brand__mark {
    width: 22px;
    height: 22px;
    background: var(--ink);
    margin-top: 14px;
  }
  .brand__name {
    font-family: 'Oswald', sans-serif;
    font-weight: 500;
    font-size: 62px;
    line-height: 0.98;
    letter-spacing: -1px;
    text-transform: uppercase;
    color: var(--ink);
    margin: 0;
  }
  .label__rule {
    position: absolute;
    left: 98px;
    right: 40px;
    top: 392px;
    height: 2px;
    background: var(--rule);
  }
  .product {
    position: absolute;
    left: 98px;
    top: 440px;
  }
  .product__name {
    font-family: 'Oswald', sans-serif;
    font-weight: 600;
    font-size: 74px;
    line-height: 1;
    letter-spacing: -1px;
    color: var(--ink);
    margin: 0;
    text-transform: uppercase;
  }
  .product__type {
    font-family: 'Oswald', sans-serif;
    font-weight: 400;
    font-size: 44px;
    line-height: 1;
    color: var(--ink-soft);
    margin: 14px 0 0;
    text-transform: uppercase;
  }
  .product__notes {
    font-family: 'Courier Prime', monospace;
    font-size: 20px;
    line-height: 1.2;
    color: var(--ink-soft);
    margin: 64px 0 0;
  }
  .product__notes b { color: var(--ink); font-weight: 700; }
  .product__size {
    font-family: 'Courier Prime', monospace;
    font-size: 17px;
    color: var(--ink-soft);
    margin: 42px 0 0;
  }
  .product__size strong {
    font-family: 'Oswald', sans-serif;
    font-size: 36px;
    font-weight: 600;
    color: var(--ink);
    margin-right: 4px;
  }
</style>
</head>
<body>
<main class="canvas">
  <section class="label" aria-label="Balancing Facial Serum label">
    <p class="label__url">www.<b>marisol</b>thackery<b>beauty</b>.example</p>

    <div class="brand">
      <h1 class="brand__name">Marisol<br>Thackery<br>Beauty</h1>
      <span class="brand__mark" aria-hidden="true"></span>
    </div>

    <div class="label__rule"></div>

    <div class="product">
      <h2 class="product__name">Balancing</h2>
      <p class="product__type">Facial Serum</p>
      <p class="product__notes"><b>a</b>dditional <b>t</b>ext:<br>Officim eum nati<br>blaborest omnim</p>
      <p class="product__size"><strong>1</strong>fl oz</p>
    </div>
  </section>
</main>
</body>
</html>
```